Tea standup pouch labels

Dear designers,
I need a minimalistic and modern label for my loose tea stand-up pouches (100, 250 and 500gm packs). The label should cover 70-80% of the pouch face (front and rear both).
The label will be 2 part label - Front and Rear side labels.
The labels should have a green background (Pantone Green C) with Golden or White or black colour text. Please either use the Golden logo or black logo to see which looks good with Pantone Green C background.
I am also attaching the content file and a few other files (plain circle badge) to be used in the label.
The plain circle badge should be small at the bottom left or right side of the front side. The logo should be dominant on the front page (some of the designs I received have small logo and big "100% single estate tea" and "Assam logo" as big characters on the front page which is not what I am looking for.

The font style should note simple Times new roman or Arial. It should look modern and should be something matching to the logo sentence 'Freshest possible' but should also not be in italics. Please refer to files Font style reference front and back for the style of font. Also use the same box space design on the rear - Content should be in White background; the rectangular box edges should be rounded and the border should be in dual colour - Golden and white or in black and white depending on the logo colour used (golden or black).

For the Rear page - headings could be in Golden colour or black colour depending on the logo colour you choose to use and the text can be in white colour i.e. Option 1 - Headings in golden colour and text in white colour; Option 2 - Heading in Black colour and text in white colour or any other combination that looks good - designer to decide.

Please let me know if you need any further information.

thanks,
Toral

```html
<!DOCTYPE html>
<html lang="en">
<head>
<meta charset="utf-8">
<title>Brewvale – Tea Pouch Labels</title>
<link rel="stylesheet" href="https://fonts.googleapis.com/css2?family=Jost:wght@300;400;500&family=Oswald:wght@500;600&family=Mrs+Saint+Delafield&display=swap">
<style>
  :root {
    --stage: #e8e8e8;
    --label-green: #33b8a6;
    --leaf-tint: #5ccab9;
    --ink: #111111;
    --white: #ffffff;
    --rule: rgba(17, 17, 17, 0.55);
  }
  * { box-sizing: border-box; margin: 0; padding: 0; }
  html, body { width: 1200px; height: 860px; overflow: hidden; }
  body {
    background: var(--stage);
    font-family: "Jost", "Futura", sans-serif;
    color: var(--white);
    position: relative;
  }
  .label {
    position: absolute;
    top: 30px;
    width: 533px;
    height: 800px;
    background: var(--label-green);
    overflow: hidden;
  }
  .label--front { left: 44px; }
  .label--rear { left: 623px; }
  .leaf-pattern {
    position: absolute; inset: 0;
    background:
      radial-gradient(ellipse 180px 90px at 20% 15%, var(--leaf-tint), transparent 70%),
      radial-gradient(ellipse 160px 80px at 80% 40%, var(--leaf-tint), transparent 70%),
      radial-gradient(ellipse 190px 90px at 25% 70%, var(--leaf-tint), transparent 70%),
      radial-gradient(ellipse 170px 80px at 78% 88%, var(--leaf-tint), transparent 70%);
    opacity: 0.55;
  }
  .label > *:not(.leaf-pattern) { position: absolute; }

  /* Front */
  .brand-mark {
    left: 0; right: 0; top: 120px;
    text-align: center; color: var(--ink);
  }
  .brand-mark__circle {
    width: 92px; height: 92px; border: 3px solid var(--ink);
    border-radius: 50%; margin: 0 auto 26px;
  }
  .brand-mark__name {
    font-family: "Jost", sans-serif; font-weight: 300;
    font-size: 66px; letter-spacing: 6px; line-height: 1;
  }
  .tagline {
    left: 0; right: 0; top: 430px; text-align: center;
    font-family: "Mrs Saint Delafield", cursive;
    font-size: 54px; color: var(--ink);
  }
  .claim {
    left: 164px; top: 512px; width: 208px; height: 88px;
    text-align: center; color: var(--ink);
    font-family: "Oswald", sans-serif; font-weight: 600;
    border-top: 3px solid var(--white);
  }
  .claim::before, .claim::after {
    content: ""; position: absolute; width: 3px; height: 16px; background: var(--white);
  }
  .claim::before { left: 0; top: 0; }
  .claim::after { right: 0; top: 0; }
  .claim__base {
    position: absolute; left: 0; right: 0; bottom: 0; height: 18px;
    border: 3px solid var(--white); border-top: none;
  }
  .claim__pct { display: block; font-size: 28px; line-height: 1; margin-top: 12px; }
  .claim__text { display: block; font-size: 27px; line-height: 1.2; letter-spacing: 0.3px; }
  .net-weight {
    left: 0; right: 0; top: 640px; text-align: center;
    font-family: "Oswald", sans-serif; font-weight: 600;
    font-size: 11px; color: var(--ink);
  }
  .origin-badge {
    left: 209px; top: 658px; width: 116px; height: 116px;
    border: 3px solid var(--white); border-radius: 50%;
  }

  /* Rear */
  .rear-title {
    left: 0; right: 0; top: 32px; text-align: center;
    font-weight: 500; font-size: 15px; letter-spacing: 0.3px;
  }
  .story {
    left: 45px; right: 42px; top: 62px;
    font-size: 9.3px; line-height: 12.4px; font-weight: 300;
    text-align: justify; text-align-last: center; color: var(--ink);
  }
  .story p + p { margin-top: 1px; }
  .section-title { font-weight: 500; font-size: 15px; letter-spacing: 0.2px; }
  .brew-guide { left: 34px; top: 205px; width: 240px; }
  .brew-guide .section-title { padding-left: 18px; margin-bottom: 10px; }
  .brew-step { display: flex; gap: 8px; margin-bottom: 12px; }
  .brew-step__icon { width: 22px; height: 16px; flex: none; }
  .brew-step__text {
    font-size: 9.3px; line-height: 12.3px; font-weight: 300;
    text-align: justify; color: var(--ink);
  }
  .nutrition {
    left: 268px; top: 205px; width: 246px;
    border-left: 1px solid rgba(255,255,255,0.5); padding-left: 10px;
  }
  .nutrition .section-title { margin-bottom: 10px; font-size: 14.5px; }
  .nutrition-table { width: 100%; border-collapse: collapse; color: var(--ink); }
  .nutrition-table th {
    font-size: 7.6px; font-weight: 500; text-align: left; padding: 0 0 5px 4px;
    border-bottom: 1px solid var(--rule);
  }
  .nutrition-table th:last-child { text-align: right; }
  .nutrition-table td {
    font-size: 8.6px; font-weight: 300; padding: 5px 4px 4px;
    border-bottom: 1px dashed var(--rule);
  }
  .nutrition-table td:last-child { text-align: right; }
  .nutrition__note { font-size: 7.2px; font-weight: 300; color: var(--ink); margin-top: 8px; }
  .storage {
    left: 0; right: 0; top: 420px; text-align: center;
  }
  .storage p { font-size: 9.3px; font-weight: 300; color: var(--ink); margin-top: 4px; }
  .fact {
    left: 45px; right: 42px;
    font-size: 9.3px; font-weight: 300; color: var(--ink); line-height: 12.5px;
  }
  .fact strong { font-weight: 500; font-size: 11.5px; color: var(--white); letter-spacing: 0.2px; }
  .fact--taste { top: 468px; }
  .fact--ingredients { top: 496px; }
  .fact--allergen { top: 523px; }
  .fact--packer { top: 557px; }
  .fact--web { top: 581px; }
  .fact--web b { font-weight: 500; }
  .fact--contact { top: 606px; }
  .info-box {
    top: 653px; height: 114px; background: var(--white); color: #333;
    font-size: 9px; font-weight: 300; line-height: 12.3px; text-align: center;
    display: flex; flex-direction: column; justify-content: center;
  }
  .info-box--batch { left: 45px; width: 201px; }
  .info-box--code { left: 278px; width: 213px; }
</style>
</head>
<body>

<section class="label label--front">
  <div class="leaf-pattern" role="img" aria-label="Faint outline illustration of tea leaves across the label"></div>

  <div class="brand-mark">
    <div class="brand-mark__circle"></div>
    <div class="brand-mark__name">BREWVALE</div>
  </div>

  <p class="tagline">freshest possible</p>

  <div class="claim">
    <span class="claim__base"></span>
    <span class="claim__pct">100%</span>
    <span class="claim__text">SINGLE ESTATE TEA</span>
  </div>

  <p class="net-weight">NET WT 250G/8.82OZ</p>

  <div class="origin-badge" role="img" aria-label="Tea origin certification badge"></div>
</section>

<section class="label label--rear">
  <div class="leaf-pattern" role="img" aria-label="Faint outline illustration of tea leaves across the label"></div>

  <h2 class="rear-title">TEA LOSES ITS FLAVOUR AND AROMA OVER TIME</h2>

  <div class="story">
    <p>Tea tastes good for 24 months after being processed in the factory. Most tea that you get in stores passes through multiple middlemen (like auction house, wholesaler, local exporter etc) and takes between 6-12 months after harvest to reach you. By then tea has already lost a lot of its flavour and aroma.</p>
    <p>We come from a family of small-scale tea growers in Assam, India and will source tea directly from our own tea estates or from similar estates like us. Hence, we are able to tell you when the tea was picked from the garden and when it was packed. By sourcing tea directly from small-scale tea estates, we are removing middlemen, giving a better price to the tea growers and reducing the time it takes to reach tea lovers like yourself.</p>
  </div>

  <div class="brew-guide">
    <h3 class="section-title">HOW DO I DRINK IT?</h3>
    <div class="brew-step">
      <svg class="brew-step__icon" viewBox="0 0 22 16" fill="none" stroke="#fff" stroke-width="1"><path d="M4 6h11v5a4 4 0 0 1-4 4H8a4 4 0 0 1-4-4z"/><path d="M15 8h2a2 2 0 0 1 0 4h-2"/></svg>
      <p class="brew-step__text">Rinse the teapot or cup with boiling water</p>
    </div>
    <div class="brew-step">
      <svg class="brew-step__icon" viewBox="0 0 22 16" fill="none" stroke="#fff" stroke-width="1"><ellipse cx="5" cy="10" rx="4" ry="2.5"/><path d="M8 9l8-7"/></svg>
      <p class="brew-step__text">Add 2 teaspoon (~2 g) of tea leaves into the teapot and then pour boiling water and cover it with the lid</p>
    </div>
    <div class="brew-step">
      <svg class="brew-step__icon" viewBox="0 0 22 16" fill="none" stroke="#fff" stroke-width="1"><circle cx="9" cy="8" r="6.5"/><path d="M9 4v4l3 2"/></svg>
      <p class="brew-step__text">Allow the tea to brew for one minute. Keep it longer for around three minutes for a stronger brew</p>
    </div>
    <div class="brew-step">
      <svg class="brew-step__icon" viewBox="0 0 22 16" fill="none" stroke="#fff" stroke-width="1"><path d="M3 7h12v3a4 4 0 0 1-4 4H7a4 4 0 0 1-4-4z"/><path d="M7 2v3M10 2v3"/></svg>
      <p class="brew-step__text">Pour the brew into a cup using a strainer</p>
    </div>
    <div class="brew-step">
      <svg class="brew-step__icon" viewBox="0 0 22 16" fill="none" stroke="#fff" stroke-width="1"><rect x="3" y="5" width="9" height="10" rx="1"/><path d="M5 5V2h5v3"/></svg>
      <p class="brew-step__text">Add milk and sugar to taste</p>
    </div>
  </div>

  <div class="nutrition">
    <h3 class="section-title">NUTRITIONAL INFORMATION:</h3>
    <table class="nutrition-table">
      <thead><tr><th>TYPICAL VALUES</th><th>PER 100ML BREWED INFUSION*</th></tr></thead>
      <tbody>
        <tr><td>Energy</td><td>&lt;4 kcal</td></tr>
        <tr><td>Fat</td><td>0 g</td></tr>
        <tr><td>Of which saturates</td><td>0 g</td></tr>
        <tr><td>Carbohydrates</td><td>0 g</td></tr>
        <tr><td>Of which sugar</td><td>0 g</td></tr>
        <tr><td>Protein</td><td>&lt;0.5 g</td></tr>
        <tr><td>Salt</td><td>0 g</td></tr>
      </tbody>
    </table>
    <p class="nutrition__note">*Based on an infusion brewed with 200ml water for 3 minutes</p>
  </div>

  <div class="storage">
    <h3 class="section-title">HOW DO I STORE IT:</h3>
    <p>Store in an airtight container made of ceramic or tin to keep the light out</p>
  </div>

  <p class="fact fact--taste"><strong>WHAT DOES IT TASTE LIKE?</strong> Strong, malty, astringent taste and aroma</p>
  <p class="fact fact--ingredients"><strong>INGREDIENTS:</strong> Black tea</p>
  <p class="fact fact--allergen"><strong>ALLERGAN INFORMATION:</strong> Made in a factory that processes nuts.</p>
  <p class="fact fact--packer">Packed in the UK by Brewvale Limited, 12 Alder Row, Reading, RG1 4XY, United Kingdom</p>
  <p class="fact fact--web">Visit our website at <b>www.brewvale.co.uk</b></p>
  <p class="fact fact--contact">Write to us at hello@brewvale.co.uk or Brewvale Limited, 12 Alder Row, Reading, RG1 4XY, United Kingdom</p>

  <div class="info-box info-box--batch">
    <span>“Blank space for sticker”</span>
    <span>Picked on: September 2019</span>
    <span>Packaged on: May 2020</span>
    <span>Best before: May 2022</span>
    <span>Tea type: Black Tea BOP</span>
    <span>Batch no. LOT/12345ABC</span>
  </div>
  <div class="info-box info-box--code">
    <span>“This space will be used for barcode”</span>
  </div>
</section>

</body>
</html>
```